Drapery & Decor Atelier Project…
I am looking for a new website design for a store front “Drapery & Decor Atelier” business. Their customer would walk in off the street to have curtains designed for their home or business. This is not an ecommerce website.
The website colors should be light blue, dark blue, white and maybe tan. Be creative.
The curtains they sell can be found at www.plvexo.example and www.dombly.example. Please use images from these two website.
Navigation:
Home
Our Studio
Our Services
Our Manufactures
PLVEXO
Dombly
Our Process
Testimonials
Refer a Client
Subscribe to our Newsletter
Our Blog – (Needed for Internet Marketing)
Contact Us
The website should have a large footer for internet marketing purposes.
Updates
Great designs. Thank you everyone. I have sent them all to the client and i am waiting for feedback. I will let everyone know as soon as possible.
Sorry for the delay everyone. The client has been on vacation and has not provided feedback yet. As soon as I have an update I will let everyone know.

```html
<!DOCTYPE html>
<html lang="en">
<head>
<meta charset="utf-8">
<title>Drapery &amp; Decor Atelier Project</title>
<link href="https://fonts.googleapis.com/css2?family=Open+Sans:wght@400;600;700&family=Arimo:wght@400;700&family=Great+Vibes&display=swap" rel="stylesheet">
<style>
:root{
  --outer:#2e2a2a;
  --page:#ffffff;
  --ink:#444444;
  --ink-soft:#555555;
  --heading:#4a4a4a;
  --blue:#1a9cc4;
  --blue-dark:#0f7fa3;
  --navy:#1d4e7a;
  --navy-deep:#143a5c;
  --tan:#c9a878;
  --tan-dark:#a8875a;
  --nav-top:#4a4a4a;
  --nav-bottom:#242424;
  --panel:#ececec;
  --footer:#2b2b2b;
  --footer-deep:#1f1f1f;
  --green:#5cae2a;
}
*{margin:0;padding:0;box-sizing:border-box}
html,body{width:975px;height:1200px;overflow:hidden;background:var(--outer)}
body{font-family:Arimo,Arial,sans-serif;color:var(--ink);position:relative}
.abs{position:absolute}
.page{left:107px;top:0;width:757px;height:956px;background:var(--page)}

/* header */
.brand{left:140px;top:25px;font-family:'Open Sans',sans-serif;font-weight:700;line-height:1}
.brand .main{font-size:25px;letter-spacing:-.6px;color:#3b3b3b}
.brand .sub{font-size:12px;margin-top:4px;color:var(--navy);font-weight:600}
.toplinks{left:655px;top:30px;width:180px;font-size:8.5px;color:#555;text-align:right;word-spacing:2px}
.search{left:380px;top:49px;width:236px;height:30px;background:#e4e4e4;border-radius:5px}
.search .field{left:6px;top:5px;width:178px;height:20px;background:#fff;border:1px solid #ccc;font-size:8.5px;color:#999;padding:5px 4px}
.search .btn{left:189px;top:5px;width:41px;height:20px;background:linear-gradient(var(--blue),var(--blue-dark));color:#fff;font-size:9.5px;font-weight:700;text-align:center;line-height:20px;border-radius:2px}
.visit{left:647px;top:51px;width:188px;height:27px;border-radius:3px;background:linear-gradient(#2a6699,var(--navy-deep));color:#fff;font-family:'Open Sans',sans-serif;font-size:9.5px;font-weight:600;line-height:27px;padding-left:27px}
.visit svg{position:absolute;left:8px;top:6px}

/* nav */
.navbar{left:112px;top:104px;width:749px;height:26px;background:linear-gradient(var(--nav-top),var(--nav-bottom))}
.nav-home{left:148px;top:102px;width:52px;height:30px;background:linear-gradient(#29aed6,var(--blue-dark))}
.nav-item{top:104px;height:26px;line-height:26px;font-family:'Open Sans',sans-serif;font-size:7.5px;font-weight:700;color:#fff;text-transform:uppercase}
.nav-sep{top:109px;width:1px;height:16px;background:#5a5a5a}

/* hero */
.hero{left:126px;top:146px;width:720px;height:274px;border:1px solid #ddd;background:#fff}
.hero-art{left:134px;top:152px;width:704px;height:262px;background:linear-gradient(90deg,#6a4a5e 0%,#4e3d62 35%,#7d6c85 62%,#cfc6b0 70%,#e6dfcd 100%)}
.hero-card{left:164px;top:187px;width:289px;height:186px;border:2px solid rgba(255,255,255,.75);border-radius:8px;background:rgba(20,20,20,.72)}
.hero-title{left:176px;top:199px;font-family:'Open Sans',sans-serif;font-size:23px;color:#fff;letter-spacing:.2px}
.hero-title span{color:#29b4e0}
.hero-text{left:178px;top:240px;width:252px;font-size:9.4px;line-height:15px;color:#eee;letter-spacing:.4px}
.hero-text b{color:#fff}
.hero-btn{left:330px;top:330px;width:87px;height:23px;border-radius:4px;background:linear-gradient(#29aed6,var(--blue-dark));color:#fff;font-family:'Open Sans',sans-serif;font-size:12px;line-height:23px;padding-left:10px}
.hero-btn i{position:absolute;right:6px;top:5px;width:13px;height:13px;border-radius:50%;background:#fff}
.badge{left:430px;top:172px}
.hero-shadow{left:126px;top:420px;width:720px;height:14px;background:radial-gradient(ellipse at top,rgba(0,0,0,.18),transparent 70%)}

/* intro */
.intro-h{left:144px;top:450px;font-family:'Open Sans',sans-serif;font-size:24px;font-weight:700;color:var(--heading)}
.intro-sub{left:145px;top:479px;font-family:'Open Sans',sans-serif;font-size:13px;font-weight:600;color:var(--blue)}
.intro-p{left:143px;width:502px;font-size:8.8px;line-height:13.6px;color:var(--ink-soft);letter-spacing:.15px}
.rule{left:124px;top:628px;width:500px;height:1px;background:linear-gradient(90deg,transparent,#ddd,transparent)}

.feature{top:652px;width:155px}
.feature h3{font-family:'Open Sans',sans-serif;font-size:14px;font-weight:600;color:var(--heading);padding-left:24px;position:relative;height:22px}
.feature h3 svg{position:absolute;left:0;top:0}
.feature p{margin-top:8px;font-size:8.8px;line-height:13.6px;color:var(--ink-soft);padding-left:2px;letter-spacing:.2px}
.dots{top:648px;width:3px;height:100px;border-left:1px dotted #bbb;border-right:1px dotted #bbb}

/* deals */
.deals{left:660px;top:444px;width:187px;height:320px;background:var(--panel);border:1px solid #ddd}
.deals-head{left:663px;top:447px;width:181px;height:35px;background:linear-gradient(#fff,#e4e4e4);font-family:'Great Vibes',cursive;font-size:25px;color:#1f7fa5;padding-left:13px;line-height:36px}
.deals-art{left:671px;top:495px;width:164px;height:100px;background:linear-gradient(90deg,#d9d4cc 0%,#b84a78 15%,#d9789e 40%,#f1eee8 55%,#b84a78 75%,#d9d4cc 100%)}
.deals-more{left:671px;top:578px;width:164px;height:17px;background:rgba(40,40,40,.8);color:#fff;font-size:8.5px;text-align:right;padding:3px 6px 0 0}
.deals-text{left:673px;top:602px;width:165px;font-size:8.8px;line-height:13px;color:#333}
.btn-sm{top:635px;height:17px;border-radius:3px;color:#fff;font-size:8.8px;line-height:17px;text-align:center}
.hours{left:670px;top:667px;width:168px;height:43px;border:1px dashed var(--tan-dark);background:linear-gradient(#fbf6ec,#ecdcc0)}
.hours .lbl{left:52px;top:6px;font-family:'Open Sans',sans-serif;font-size:10px;font-weight:700;color:#333}
.hours .val{left:52px;top:20px;font-family:'Open Sans',sans-serif;font-size:14px;font-weight:700;color:var(--navy)}
.hours svg{position:absolute;left:9px;top:4px}
.listing{top:725px;height:25px;border-radius:2px}

/* carousel */
.strip{left:126px;top:778px;width:718px;height:129px;background:#e6e6e6}
.thumb{top:786px;width:151px;height:110px;border:2px solid #fff;box-shadow:0 3px 5px rgba(0,0,0,.2)}
.arrow{top:830px}

/* social tab */
.tab{left:107px;top:920px}
.social-label{left:175px;top:941px;font-family:'Open Sans',sans-serif;font-size:13px;font-weight:700;color:#fff}
.soc{top:940px;width:18px;height:18px;border-radius:4px}

/* footer */
.footer{left:107px;top:956px;width:757px;height:136px;background:var(--footer)}
.sub-label{left:184px;top:983px;font-family:'Open Sans',sans-serif;font-size:11px;font-weight:600;color:#e4e4e4}
.email{left:182px;top:1005px;width:176px;height:18px;border-radius:9px;background:linear-gradient(#8c8c8c,#6b6b6b);color:#f2f2f2;font-style:italic;font-size:9.5px;line-height:18px;padding-left:10px}
.email i{position:absolute;right:6px;top:3px;width:22px;height:12px;background:#ccc;border-radius:2px}
.copy{left:174px;top:1046px;width:184px;height:46px;background:#242424;border-radius:10px 10px 0 0}
.copy .ring{left:12px;top:12px;width:24px;height:24px;border-radius:50%;border:3px solid #ddd}
.copy p{position:absolute;left:44px;top:12px;font-size:8.3px;line-height:15px;color:#ddd}
.fnav-h{left:419px;top:970px;font-family:'Open Sans',sans-serif;font-size:15px;font-weight:600;color:#fff;letter-spacing:.5px}
.fnav{top:998px;list-style:none;font-family:'Open Sans',sans-serif;font-size:9.3px;color:#eee}
.fnav li{height:16.5px;padding-left:10px;position:relative}
.fnav li::before{content:"";position:absolute;left:0;top:3px;border-left:5px solid var(--blue);border-top:3.5px solid transparent;border-bottom:3.5px solid transparent}
.contact-h{left:660px;top:969px;width:187px;text-align:right;font-family:'Open Sans',sans-serif;font-size:12.5px;color:var(--tan);letter-spacing:.3px}
.contact{left:600px;top:997px;width:244px;text-align:right;font-size:9.3px;line-height:15.2px;color:#fff}
.bottom-band{left:107px;top:1092px;width:757px;height:108px;background:var(--footer-deep)}
.bottom-brand{left:127px;top:1106px;font-family:'Open Sans',sans-serif;font-size:15.5px;color:var(--blue)}
.bottom-brand span{color:#cfcfcf}
.partners{left:370px;top:1102px;width:474px;height:32px;background:#fff}
.partner{top:1110px;height:15px;background:#4a4a4a;border-radius:2px}
.legal{left:120px;top:1150px;width:722px;text-align:right;font-size:7.8px;line-height:12px;color:#bdbdbd}
</style>
</head>
<body>
<div class="abs page"></div>

<!-- header -->
<div class="abs brand"><div class="main">Drapery &amp; Decor</div><div class="sub">Atelier Project</div></div>
<div class="abs toplinks">My Account &nbsp;|&nbsp; Our Blog &nbsp;|&nbsp; Contact Us</div>
<div class="abs search"><div class="abs field">Enter Keyword or item#</div><div class="abs btn">Search</div></div>
<div class="abs visit"><svg width="14" height="14" viewBox="0 0 14 14"><rect x="1" y="2.5" width="12" height="10.5" rx="1" fill="none" stroke="#fff" stroke-width="1.4"/><path d="M1 6h12M4 1v3M10 1v3" stroke="#fff" stroke-width="1.4"/></svg>Book a studio visit | Saved designs</div>

<!-- navigation -->
<div class="abs navbar"></div>
<div class="abs nav-home"></div>
<div class="abs nav-item" style="left:160px">Home</div>
<div class="abs nav-item" style="left:214px">Our Studio</div>
<div class="abs nav-sep" style="left:278px"></div>
<div class="abs nav-item" style="left:292px">Our Services</div>
<div class="abs nav-sep" style="left:362px"></div>
<div class="abs nav-item" style="left:376px">Our Manufactures</div>
<div class="abs nav-sep" style="left:474px"></div>
<div class="abs nav-item" style="left:488px">PLVEXO</div>
<div class="abs nav-sep" style="left:537px"></div>
<div class="abs nav-item" style="left:553px">Dombly</div>
<div class="abs nav-sep" style="left:597px"></div>
<div class="abs nav-item" style="left:611px">Our Process</div>

<!-- hero -->
<div class="abs hero"></div>
<div class="abs hero-art" role="img" aria-label="Bedroom interior with plum curtains beside a window with leaf-patterned drapes"></div>
<div class="abs hero-card"></div>
<div class="abs hero-title">Curtains &amp; <span>Curtain Rods.</span></div>
<div class="abs hero-text"><b>Delay the arrival</b> of dawn with curtains that block, soften or change the colour of the sunlight and bring a new mood to every room Delay the arrival of dawn with curtains that block, soften or change the colour of the sunlight a new mood to every room.</div>
<div class="abs hero-btn">Visit Us<i></i></div>
<svg class="abs badge" width="66" height="66" viewBox="0 0 66 66"><polygon points="33,2 39,10 49,6 51,16 61,18 57,27 64,34 56,40 59,50 49,51 46,61 37,57 30,64 25,56 15,58 14,48 4,45 9,36 3,28 12,23 11,13 21,13 25,4" fill="#1e9fd0" stroke="#fff" stroke-width="1.5"/><text x="33" y="31" text-anchor="middle" font-family="Open Sans,sans-serif" font-weight="700" font-size="11" fill="#fff" transform="rotate(-20 33 33)">FREE</text><text x="33" y="44" text-anchor="middle" font-family="Open Sans,sans-serif" font-weight="700" font-size="11" fill="#fff" transform="rotate(-20 33 33)">QUOTE</text></svg>
<div class="abs hero-shadow"></div>

<!-- intro -->
<h1 class="abs intro-h">Curtains</h1>
<h2 class="abs intro-sub">Cheltenham, Tewkesbury, The Cotswolds &amp; Gloucestershire.</h2>
<p class="abs intro-p" style="top:503px">At Hollis Marlowe Interiors we have an experienced and fully qualified interior designer who can help you obtain the professionally styled room that you have always wanted to have. Our interior designer will find you the right curtains, blinds and soft furnishings as detailed below that combine to create a remarkable interior design.</p>
<p class="abs intro-p" style="top:556px">As well as supplying and installing various types of flooring to customers we can supply you with soft furnishings, curtains, blinds and more for the home. All of our interior furnishings are of the highest quality and are produced by some of the worlds top brands. Browse through our galleries below to get a taste of what we can offer, or visit one of our manufacturer's websites for more information.</p>
<div class="abs rule"></div>

<div class="abs feature" style="left:144px;top:654px"><h3><svg width="22" height="18" viewBox="0 0 22 18"><path d="M2 9l6 6L20 2" fill="none" stroke="#5cae2a" stroke-width="4" stroke-linecap="round"/></svg>Best Privacy</h3><p>Easy to hang, use and take down, useable on 100% of all existing tracks.Our disposable curtains are designed.</p></div>
<div class="abs dots" style="left:296px"></div>
<div class="abs feature" style="left:312px"><h3><svg width="22" height="18" viewBox="0 0 22 18"><path d="M2 9l6 6L20 2" fill="none" stroke="#5cae2a" stroke-width="4" stroke-linecap="round"/></svg>Best Protection</h3><p>Easy to hang, use and take down, useable on 100% of all existing tracks.Our disposable curtains are designed.</p></div>
<div class="abs dots" style="left:465px"></div>
<div class="abs feature" style="left:485px"><h3><svg width="22" height="18" viewBox="0 0 22 18"><path d="M2 9l6 6L20 2" fill="none" stroke="#5cae2a" stroke-width="4" stroke-linecap="round"/></svg>Best Price</h3><p>Easy to hang, use and take down, useable on 100% of all existing tracks.Our disposable curtains are designed.</p></div>

<!-- special deals -->
<div class="abs deals"></div>
<div class="abs deals-head">Special Deals</div>
<div class="abs deals-art" role="img" aria-label="Patterned curtains hung on a rod"></div>
<div class="abs deals-more">View more <b>[+]</b></div>
<p class="abs deals-text">Lorem Ipsum is simply dummy text of the printing and typesetting industry</p>
<div class="abs btn-sm" style="left:673px;width:55px;background:linear-gradient(#29aed6,var(--blue-dark))">Enquire</div>
<div class="abs btn-sm" style="left:778px;width:42px;background:#3a3a3a">More</div>
<div class="abs hours"><svg width="36" height="36" viewBox="0 0 36 36"><circle cx="18" cy="18" r="17" fill="#333"/><circle cx="18" cy="18" r="13" fill="#f4f4f4"/><path d="M18 9v9l6 3" stroke="#222" stroke-width="2" fill="none"/></svg><div class="abs lbl">Studio Open</div><div class="abs val">Mon–Sat 9–5</div></div>
<div class="abs listing" style="left:669px;width:84px;background:linear-gradient(#5f6f86,#3d4a5e)"></div>
<div class="abs listing" style="left:759px;width:84px;background:#e8e8e8;border:1px solid #ccc"></div>

<!-- carousel -->
<div class="abs strip"></div>
<div class="abs thumb" style="left:153px;background:linear-gradient(90deg,#d8c23a,#f0dc4a 30%,#c9d6c8 50%,#f0dc4a 70%,#d8c23a)" role="img" aria-label="Yellow tab-top curtains"></div>
<div class="abs thumb" style="left:329px;background:linear-gradient(#e9e2d6,#b89f85 60%,#5a3a2a)" role="img" aria-label="Cream swag curtains over French doors in a living room"></div>
<div class="abs thumb" style="left:498px;background:linear-gradient(90deg,#e4b08c,#f1c8a6 50%,#e4b08c)" role="img" aria-label="Peach sheer café curtains on a window"></div>
<div class="abs thumb" style="left:666px;background:linear-gradient(#6a3a2a,#b57a4a 50%,#5a3020)" role="img" aria-label="Rich brown drapes in a formal lounge"></div>
<svg class="abs arrow" style="left:128px" width="20" height="28" viewBox="0 0 20 28"><path d="M16 2L4 14l12 12" fill="none" stroke="#777" stroke-width="5"/></svg>
<svg class="abs arrow" style="left:820px" width="20" height="28" viewBox="0 0 20 28"><path d="M4 2l12 12L4 26" fill="none" stroke="#777" stroke-width="5"/></svg>

<!-- social tab -->
<svg class="tab abs" width="757" height="37" viewBox="0 0 757 37"><path d="M0 36H37Q45 36 48 26L55 10Q60 2 70 2H300Q310 2 315 10L322 26Q326 36 334 36H757" fill="#2b2b2b" stroke="#cfcfcf" stroke-width="3"/><rect x="0" y="36" width="757" height="1" fill="#2b2b2b"/><path d="M40 37L49 25 56 10Q61 3 70 3H300Q309 3 314 10L321 25 331 37Z" fill="#2b2b2b"/></svg>
<div class="abs social-label">Socialize with us:</div>
<div class="abs soc" style="left:299px;background:#e8701e"></div>
<div class="abs soc" style="left:327px;background:#3aa7de"></div>
<div class="abs soc" style="left:355px;background:#3a5a98"></div>
<div class="abs soc" style="left:382px;background:#1f6fa8"></div>

<!-- footer -->
<div class="abs footer"></div>
<div class="abs sub-label">Subscribe to our Newsletter</div>
<div class="abs email">Your E-Mail Address<i></i></div>
<div class="abs copy"><div class="abs ring"></div><p>@ 2012 Drapery &amp; Decor Atelier<br>All Right Reserved.</p></div>

<div class="abs fnav-h">Navigation</div>
<ul class="abs fnav" style="left:419px"><li>Home</li><li>Our Studio</li><li>Our Services</li><li>Our Manufactures</li><li>PLVEXO Dombly</li></ul>
<ul class="abs fnav" style="left:534px"><li>Our Process</li><li>Testimonials</li><li>Refer a Client</li><li>Our Blog</li><li>Contact Us</li></ul>

<div class="abs contact-h">CONTACT INFORMATION</div>
<div class="abs contact"><b style="font-size:10.5px">Harlow's Corner Shop</b><br>48 Larchmont Road<br>Austrailia<br><b>4Hr. Tel. :</b> 08 5550 1947<br><b>Email:</b> hello@harlowcorner.example</div>

<div class="abs bottom-band"></div>
<div class="abs bottom-brand">Drapery &amp; Decor <span>Atelier Project</span></div>
<div class="abs partners"></div>
<div class="abs partner" style="left:378px;width:44px"></div>
<div class="abs partner" style="left:440px;width:40px;background:#8a8a8a"></div>
<div class="abs partner" style="left:505px;width:36px"></div>
<div class="abs partner" style="left:556px;width:36px;background:#333"></div>
<div class="abs partner" style="left:608px;width:24px;top:1106px;height:22px;border:2px solid #333;background:none"></div>
<div class="abs partner" style="left:650px;width:36px;background:#555"></div>
<div class="abs partner" style="left:700px;width:32px;background:none;border:1px solid #555"></div>
<div class="abs partner" style="left:752px;width:24px;top:1105px;height:24px;background:#777"></div>
<div class="abs partner" style="left:795px;width:40px;background:#333"></div>

<div class="abs legal">Wood Flooring | About Us | Curtains, Blinds &amp; Furnishings | Curtain Makers | Curtains | Roman Blinds | Interior Design | Wooden Flooring | Laminate | Carpets | Larnell &amp; Omtiva |<br>Commercial | Testimonials | Floor Preparation | Gallery | Kitchens and Bathrooms | Contact Us | Resources | Sitemap | XML Sitemap<br>© Copyright 2012 - Drapery &amp; Decor Atelier Project - All Rights Reserved - Privacy &amp; Cookies Policy - Wood Flooring Cheltenham - Company No. 04718826</div>
</body>
</html>
```